TARPLOAD business card design

TARPLOAD is a manufacturer of skip bags supplying both the domestic and commercial market. We wish to convey core characteristics of strength, professionalism and reliability to our customers. We are after a business card that uses our company colours of black and yellow as well as incorporating our logo. Our customers are predominantly in the construction or hardware industry. It is important the cards are professional as we are a small company wishing to appear larger than we actually are. more info on the company and product available at www.tarpload-example.com.au

Target Market(s)

hardware buyers, contruction company owners

Industry/Entity Type

Construction

Requirements
Must have
• company colours of black and yellow - No other colours or variation of yellow black. our company logo. card design must convey "tough"
• Card design must be landscape
• Details to be included on the card are:
• Name and Tiltle
• Phone number : 1300 41 62 53
• Mobile: 0452 718 903
• Fax: 03 9617 4852
• email: dale.hendry@tarpload-example.com.au
• address: PO Box 517, Kelvindale, VIC,3294
• Text in white when on a black background
Nice to have
• I like the idea of the back of the card being black with lighter circle area in the middle with black logo in the centre. Similar to the attached "iconic" card

```html
<!DOCTYPE html>
<html lang="en">
<head>
<meta charset="utf-8">
<title>TARPLOAD business card</title>
<link rel="stylesheet" href="https://fonts.googleapis.com/css2?family=PT+Sans:wght@400;700&display=swap">
<style>
  :root {
    --page: #e4e4e4;
    --yellow: #f2c200;
    --black: #0d0d0d;
    --white: #ffffff;
    --grey-edge: #6e6e6e;
    --grey-centre: #dcdcdc;
    --card-line: #3a3a3a;
  }
  * { box-sizing: border-box; margin: 0; padding: 0; }
  html, body {
    width: 1200px;
    height: 683px;
    overflow: hidden;
    background: var(--page);
    font-family: "PT Sans", Arial, sans-serif;
  }
  .sheet {
    width: 1200px;
    height: 683px;
    display: flex;
    align-items: center;
    justify-content: center;
    gap: 60px;
  }
  .card {
    position: relative;
    width: 540px;
    height: 236px;
    border: 1px solid var(--card-line);
    overflow: hidden;
  }

  /* Front */
  .card-front { background: var(--yellow); }
  .brand {
    position: absolute;
    left: 40px;
    top: 100px;
    display: flex;
    align-items: center;
    gap: 8px;
  }
  .brand-mark {
    width: 22px;
    height: 22px;
    background: var(--black);
  }
  .brand-name {
    font-weight: 700;
    font-size: 30px;
    letter-spacing: 0.5px;
    color: var(--black);
    line-height: 1;
  }
  .contact-panel {
    position: absolute;
    left: 238px;
    top: 72px;
    right: 0;
    height: 88px;
    background: var(--black);
    border-bottom-left-radius: 22px;
    box-shadow: 4px 8px 8px rgba(0, 0, 0, 0.35);
    padding: 5px 0 0 23px;
    list-style: none;
  }
  .contact-panel li {
    font-size: 12.5px;
    line-height: 16.5px;
    color: var(--white);
    white-space: nowrap;
  }
  .contact-panel .label { color: var(--yellow); font-size: 13.5px; }
  .contact-panel .value { font-size: 11.5px; }

  /* Back */
  .card-back {
    background: radial-gradient(ellipse 60% 75% at 50% 42%, var(--grey-centre) 0%, #b8b8b8 45%, var(--grey-edge) 100%);
    display: flex;
    align-items: center;
    justify-content: center;
  }
  .card-back .brand { position: static; gap: 12px; }
  .card-back .brand-mark { width: 34px; height: 34px; }
  .card-back .brand-name { font-size: 50px; }
</style>
</head>
<body>
  <main class="sheet">
    <section class="card card-front" aria-label="Card front">
      <div class="brand">
        <span class="brand-mark"></span>
        <span class="brand-name">TARPLOAD</span>
      </div>
      <ul class="contact-panel">
        <li><span class="label">Phone number:</span> <span class="value">1300 41 62 53</span></li>
        <li><span class="label">Mobile:</span> <span class="value">0452 718 903</span></li>
        <li><span class="label">Fax:</span> <span class="value">03 9617 4852</span></li>
        <li><span class="label">email:</span> <span class="value">dale.hendry@tarpload-example.com.au</span></li>
        <li><span class="label">address:</span> <span class="value">PO Box 517, Kelvindale, VIC,3294</span></li>
      </ul>
    </section>
    <section class="card card-back" aria-label="Card back">
      <div class="brand">
        <span class="brand-mark"></span>
        <span class="brand-name">TARPLOAD</span>
      </div>
    </section>
  </main>
</body>
</html>
```